Meridale Tax Advisers Business Card

We are seeking a clean, professional, and modern double sided business card design for Meridale Tax Advisers, a tax, accounting, and advisory firm serving business owners, professionals, and investors.
The design should convey credibility, precision, trust, and sophistication appropriate for a CPA level tax advisory firm. Avoid playful, trendy, or overly decorative styles. The look should be sharp, balanced, and timeless.
Our official company logo has been uploaded, which must be incorporated appropriately and consistently with the brand. Designers should not modify, distort, or recreate the logo.
Card format
Standard US business card size (3.5 x 2 inches)
Double sided
Design direction
Professional and modern
Minimalist and uncluttered
Strong typography and clean spacing
Subtle visual interest is welcome, but simplicity is preferred
High contrast and readability are critical
Front side
Primary focus on the Meridale Tax Advisers logo
The firm name should be clearly legible and visually prominent
Background may be white or dark, depending on what best complements the logo
Back side
Contact information layout, such as
Name: Peter L. Garnick, MSA, CFP®, AIF®, EA
Title: Managing Director, Tax
Email: pgarnick@mymeridale.example
Website: https://www.meridale.example/
Mobile: (555) 318-2047
Direct: (555) 642-7130
Main: (555) 642-7188
Address: 2870 Fenwick Rd., Suite 415, Larkmoor, TX 00000
Icons may be used sparingly if they enhance clarity
The layout should feel organized and structured
Color and style
Use colors that complement the uploaded logo
Neutral, professional tones preferred
Avoid loud or saturated colors
The design should print well on standard cardstock
Print considerations
Design should be print‑ready
No edge to edge elements that risk being cut off
Proper margins and bleed awareness
Overall, the goal is a polished, high end business card that reflects trust, expertise, and professionalism consistent with a firm providing tax strategy, compliance, and advisory services.

```html
<!DOCTYPE html>
<html lang="en">
<head>
<meta charset="utf-8">
<title>Meridale Tax Advisers – Business Card</title>
<link href="https://fonts.googleapis.com/css2?family=Montserrat:wght@400;500;600;700&display=swap" rel="stylesheet">
<style>
  :root {
    --stage: #2a2a2c;
    --navy: #1f2358;
    --navy-card: #22265f;
    --navy-emboss: #2e3378;
    --orange: #f26a1b;
    --ink: #1c1c24;
    --paper: #ffffff;
  }
  * { margin: 0; padding: 0; box-sizing: border-box; }
  html, body {
    width: 1200px; height: 875px; overflow: hidden;
    background: var(--stage);
    font-family: "Montserrat", sans-serif;
  }
  .sheet {
    width: 1200px; height: 875px;
    display: flex; flex-direction: column;
    align-items: center; justify-content: center; gap: 48px;
  }
  .card {
    width: 600px; height: 343px;
    border-radius: 22px;
    position: relative;
    overflow: hidden;
  }
  /* Front */
  .card-front {
    background: var(--navy-card);
    display: flex; align-items: center; justify-content: center; gap: 16px;
  }
  .front-mark {
    width: 22px; height: 22px; border-radius: 50%;
    background: var(--navy-emboss);
    flex: none;
  }
  .front-name {
    color: var(--navy-emboss);
    font-weight: 600; font-size: 36px; letter-spacing: 3px;
    white-space: nowrap;
  }
  /* Back */
  .card-back {
    background: var(--paper);
    padding: 34px 40px;
    color: var(--ink);
  }
  .brand {
    display: flex; align-items: center; gap: 10px;
    margin-bottom: 20px;
  }
  .brand-dot { width: 14px; height: 14px; border-radius: 50%; background: var(--navy); flex: none; }
  .brand-name { color: var(--navy); font-weight: 700; font-size: 22px; letter-spacing: 1.5px; white-space: nowrap; }
  .person-line { white-space: nowrap; }
  .person-name { color: var(--navy); font-weight: 700; font-size: 21px; }
  .credentials { color: var(--orange); font-weight: 600; font-size: 13px; }
  .person-title { font-size: 13px; font-weight: 500; margin-top: 3px; }
  .address { font-size: 12.5px; line-height: 1.45; margin-top: 22px; }
  .contacts { list-style: none; margin-top: 14px; font-size: 12.5px; }
  .contacts li { display: flex; align-items: center; gap: 10px; line-height: 1.5; white-space: nowrap; }
  .contacts svg { width: 13px; height: 13px; flex: none; }
</style>
</head>
<body>
<main class="sheet">
  <section class="card card-front" aria-label="Card front">
    <span class="front-mark"></span>
    <span class="front-name">Meridale Tax Advisers</span>
  </section>

  <section class="card card-back" aria-label="Card back">
    <div class="brand">
      <span class="brand-dot"></span>
      <span class="brand-name">Meridale Tax Advisers</span>
    </div>
    <p class="person-line"><span class="person-name">Peter L. Garnick,</span> <span class="credentials">MSA, CFP®, AIF®, EA</span></p>
    <p class="person-title">Managing Director, Tax</p>
    <p class="address">2870 Fenwick Rd., Suite 415<br>Larkmoor, TX 00000</p>
    <ul class="contacts">
      <li>
        <svg viewBox="0 0 16 16" fill="none" stroke="#f26a1b" stroke-width="1.6"><rect x="4" y="1.5" width="8" height="13" rx="1.5"/><line x1="7" y1="12" x2="9" y2="12"/></svg>
        (555) 318-2047
      </li>
      <li>
        <svg viewBox="0 0 16 16" fill="#f26a1b"><path d="M3.5 1.5l2.5 0 1 3.5-1.6 1.2a8 8 0 0 0 4.4 4.4L11 9l3.5 1v2.5c0 1-1 2-2 2A11 11 0 0 1 1.5 3.5c0-1 1-2 2-2z"/></svg>
        (555) 642-7130
      </li>
      <li>
        <svg viewBox="0 0 16 16" fill="#f26a1b"><path d="M1 6c0-2 3-3.5 7-3.5S15 4 15 6v1.5h-3.5V6h-7v1.5H1z"/><rect x="3" y="8.5" width="10" height="6" rx="1"/></svg>
        (555) 642-7188
      </li>
      <li>
        <svg viewBox="0 0 16 16" fill="#f26a1b"><rect x="1" y="3" width="14" height="10" rx="1"/><path d="M1.5 3.5 8 9l6.5-5.5" fill="none" stroke="#fff" stroke-width="1.3"/></svg>
        pgarnick@mymeridale.example
      </li>
      <li>
        <svg viewBox="0 0 16 16" fill="none" stroke="#f26a1b" stroke-width="1.5"><circle cx="8" cy="8" r="6.5"/><ellipse cx="8" cy="8" rx="2.8" ry="6.5"/><line x1="1.5" y1="8" x2="14.5" y2="8"/></svg>
        www.meridale.example
      </li>
    </ul>
  </section>
</main>
</body>
</html>
```